Simple+Professional tech feel + warm and friendly box design for pet test kit

Project Name: 10-Minute Canine & Feline Rapid Test Kit Packaging Design
Target Brand Reference: VETRALUX (South Korea) styles
Design Style Direction: Professional tech feel + warm and friendly
Professionalism (Professional): Clear typography and distinct information hierarchy to reflect the product’s scientific rigor and accuracy.
Technological: Reflected through clean graphics and a minimalist layout.
Friendly: Utilise soft, warm colour combinations to convey care for pets and well-wishes for their health.
International: The design should align with mainstream aesthetics and avoid cultural ambiguities.

Target Market(s)
European Union and the United States
Industry/Entity Type
Veterinary Medical
Look and feel
Each slider illustrates characteristics of the customer's brand and the style your logo design should communicate.

```html
<!DOCTYPE html>
<html lang="en">
<head>
<meta charset="utf-8">
<title>VitaCue Rapid Test Kit – Box Dieline</title>
<link href="https://fonts.googleapis.com/css2?family=Montserrat:wght@400;500;600;700&family=Source+Sans+3:wght@400&display=swap" rel="stylesheet">
<style>
  :root{
    --board:#f2f1ef;
    --cut:#9a9a9a;
    --bleed:#f39a9a;
    --ink:#111111;
    --teal:#8fcdc2;
    --teal-soft:#c3e6df;
    --teal-pale:#e3f2ef;
    --note:#4f7f76;
    --white:#ffffff;
  }
  *{margin:0;padding:0;box-sizing:border-box}
  html,body{width:1200px;height:1200px;overflow:hidden;background:var(--white)}
  .canvas{position:relative;width:1200px;height:1200px;font-family:"Montserrat",sans-serif;color:var(--ink)}
  .dieline{position:absolute;left:0;top:0}
  .size-label{position:absolute;left:808px;top:238px;font-family:"Source Sans 3",sans-serif;font-size:19px}
  .abs{position:absolute;white-space:nowrap}
  .brand-lid{left:134px;top:378px;font-size:60px;font-weight:600;letter-spacing:.5px}
  .tm{font-size:.42em;vertical-align:top;position:relative;top:.15em;margin-left:4px;font-weight:500}
  .brand-front{left:115px;top:627px;font-size:52px;font-weight:700}
  .brand-back{left:643px;top:534px;font-size:45px;font-weight:600}
  .badge{background:#a8d9cf;font-size:17px;font-weight:500;text-align:center;line-height:26px}
  .badge-front{left:320px;top:544px;width:103px;height:26px}
  .badge-back{left:878px;top:547px;width:84px;height:21px;font-size:14px;line-height:21px}
  .maker-front{left:115px;top:718px;font-size:25px;font-weight:500}
  .maker-back{left:834px;top:713px;font-size:27px;font-weight:600}
  .company{left:459px;top:535px;font-size:12px;font-weight:700}
  .made-by{left:459px;top:553px;font-size:10px}
  .tagline{left:459px;top:579px;font-size:15px;font-weight:700;line-height:17px}
  .contact{left:459px;top:634px;width:100px;height:35px;border:1px solid #bdbdbd;border-radius:2px;font-size:8px;padding:4px 0 0 8px;line-height:15px}
  .contact span{display:flex;align-items:center;gap:5px}
  .note{left:459px;top:688px;font-size:8px;font-weight:500;color:var(--note);line-height:13px}
  .note span{padding-left:2px}
  .subtitle{left:643px;top:582px;font-size:15px;font-weight:600;line-height:18px}
  .species{left:643px;top:637px;font-size:16px;font-weight:500}
  .story{left:1067px;top:640px;width:200px;transform:translate(-50%,-50%) rotate(-90deg);font-size:10.5px;line-height:15px;text-align:center;white-space:normal}
  .art{position:absolute;border-radius:10px}
  .art-pets-front{left:114px;top:539px;width:92px;height:54px;background:linear-gradient(90deg,#dcdcdc,#e9e9e9)}
  .art-pets-back{left:842px;top:609px;width:114px;height:66px;background:linear-gradient(90deg,#d7e9e5,#cfe6e1)}
  .art-dog-faint{left:653px;top:663px;width:72px;height:84px;background:linear-gradient(180deg,#e2e2e2,#d9dedd);border-radius:30px 30px 12px 12px;opacity:.8}
  .art-molecule{left:355px;top:575px;width:91px;height:131px;border-radius:40px;background:radial-gradient(circle at 50% 45%,#9a9a9a 0%,#c9d6d3 55%,rgba(175,218,210,0) 75%)}
</style>
</head>
<body>
<div class="canvas">
  <div class="size-label">Size: 135*65*90mm</div>

  <svg class="dieline" width="1200" height="1200" viewBox="0 0 1200 1200">
    <defs>
      <linearGradient id="front-panel" x1="0" y1="0" x2="1" y2="1">
        <stop offset="0" stop-color="#f4f4f3"/>
        <stop offset=".45" stop-color="#f7f8f8"/>
        <stop offset="1" stop-color="#cfe9e4"/>
      </linearGradient>
      <linearGradient id="back-panel" x1="0" y1="0" x2="0.6" y2="1">
        <stop offset="0" stop-color="#f4f4f3"/>
        <stop offset=".4" stop-color="#f8f9f9"/>
        <stop offset="1" stop-color="#b9e0d8"/>
      </linearGradient>
      <linearGradient id="front-band" x1="0" y1="0" x2="1" y2="0">
        <stop offset="0" stop-color="#8fcdc2"/>
        <stop offset="1" stop-color="#c2e5de"/>
      </linearGradient>
      <linearGradient id="side-panel" x1="0" y1="0" x2="1" y2="1">
        <stop offset="0" stop-color="#cfe8e3"/>
        <stop offset="1" stop-color="#e4f2ef"/>
      </linearGradient>
      <g id="net">
        <path d="M86,333 Q86,316 103,316 L429,316 Q446,316 446,333 L446,521 L86,521 Z"/>
        <path d="M446,521 L456,512 L456,436 L588,436 Q594,436 596,442 L611,507 L619,521 Z"/>
        <path d="M979,521 L988,507 L1006,436 L1144,436 L1144,507 L1153,521 Z"/>
        <path d="M54,530 L86,521 L86,761 L54,753 Z"/>
        <rect x="86" y="521" width="1067" height="240"/>
        <path d="M86,761 L86,884 Q86,891 93,891 L170,891 Q177,891 177,884 L177,848 L356,848 L356,884 Q356,891 363,891 L446,891 L446,761 Z"/>
        <path d="M446,761 L533,850 L533,874 Q533,881 540,881 L619,881 L619,761 Z"/>
        <path d="M619,761 L710,848 L710,884 Q710,891 717,891 L882,891 Q889,891 889,884 L889,848 L979,761 Z"/>
        <path d="M979,761 L979,881 L1059,881 Q1066,881 1066,874 L1066,850 L1153,761 Z"/>
      </g>
    </defs>

    <!-- outer bleed line -->
    <use href="#net" fill="none" stroke="var(--bleed)" stroke-width="17" stroke-linejoin="round"/>
    <use href="#net" fill="none" stroke="var(--white)" stroke-width="15" stroke-linejoin="round"/>
    <!-- board -->
    <use href="#net" fill="var(--board)" stroke="var(--cut)" stroke-width=".8"/>

    <!-- panel artwork -->
    <rect class="panel-front" x="86" y="521" width="360" height="240" fill="url(#front-panel)"/>
    <rect class="band-front" x="86" y="706" width="360" height="55" fill="url(#front-band)"/>
    <rect class="panel-back" x="619" y="521" width="360" height="240" fill="url(#back-panel)"/>
    <rect class="panel-side-story" x="979" y="521" width="174" height="240" fill="url(#side-panel)"/>
    <path class="story-card" d="M1000,537 H1134 V714 Q1134,744 1104,744 H1000 Z" fill="var(--white)" opacity=".85" transform="translate(0,0)"/>

    <!-- tuck slits -->
    <path d="M86,348 H115 V362 M446,348 H417 V362" fill="none" stroke="var(--cut)" stroke-width=".8"/>

    <!-- fold lines -->
    <g fill="none" stroke="#9a9a9a" stroke-width=".7" stroke-dasharray="3 2">
      <line x1="86" y1="521" x2="1153" y2="521"/>
      <line x1="86" y1="761" x2="1153" y2="761"/>
      <line x1="86" y1="521" x2="86" y2="761"/>
      <line x1="446" y1="521" x2="446" y2="761"/>
      <line x1="619" y1="521" x2="619" y2="761"/>
      <line x1="979" y1="521" x2="979" y2="761"/>
    </g>

    <!-- regulatory symbols -->
    <g class="symbols" fill="none" stroke="var(--ink)" stroke-width="1">
      <circle cx="467" cy="734" r="9"/>
      <text x="467" y="739" font-family="Montserrat,sans-serif" font-size="12" font-weight="700" text-anchor="middle" fill="var(--ink)" stroke="none">2</text>
      <path d="M486,732 Q495,720 504,732 Z" fill="var(--ink)"/>
      <path d="M495,732 V742 Q495,745 492,743"/>
      <circle cx="522" cy="737" r="4"/>
      <path d="M522,729 V731 M522,743 V745 M514,737 H516 M528,737 H530 M516,731 L517.5,732.5 M528,731 L526.5,732.5 M516,743 L517.5,741.5 M528,743 L526.5,741.5 M517,742 L527,732"/>
      <rect x="535" y="730" width="32" height="16"/>
      <text x="551" y="743" font-family="Montserrat,sans-serif" font-size="12" text-anchor="middle" fill="var(--ink)" stroke="none">IVD</text>
      <path d="M578,742 H585 L590,729 H597 M588,734 V743"/>
      <circle cx="588" cy="745" r="1.6" fill="var(--ink)"/>
      <text x="572" y="744" font-family="Montserrat,sans-serif" font-size="4" fill="var(--ink)" stroke="none">4℃</text>
      <text x="598" y="731" font-family="Montserrat,sans-serif" font-size="4" fill="var(--ink)" stroke="none">30℃</text>
    </g>
  </svg>

  <!-- lid -->
  <div class="abs brand-lid">VitaCue<span class="tm">TM</span></div>

  <!-- front panel -->
  <div class="art art-pets-front" role="img" aria-label="Line drawing of a sitting dog and cat"></div>
  <div class="abs badge badge-front">5 Tests/Kit</div>
  <div class="art art-molecule" role="img" aria-label="Molecular network graphic of linked dots"></div>
  <div class="abs brand-front">VitaCue<span class="tm">TM</span></div>
  <div class="abs maker-front">Orvella</div>

  <!-- info side -->
  <div class="abs company">Orvella Biotech Limited</div>
  <div class="abs made-by">Made by Orvella</div>
  <div class="abs tagline">Aclear View into<br>Pet Health</div>
  <div class="abs contact">
    <span>
      <svg width="9" height="7" viewBox="0 0 9 7"><rect x=".5" y=".5" width="8" height="6" fill="none" stroke="#111" stroke-width=".9"/><path d="M.5,.5 L4.5,4 L8.5,.5" fill="none" stroke="#111" stroke-width=".9"/></svg>
      sales@orvellabio.com
    </span>
    <span>
      <svg width="9" height="9" viewBox="0 0 9 9"><circle cx="4.5" cy="4.5" r="4" fill="none" stroke="#111" stroke-width=".9"/><ellipse cx="4.5" cy="4.5" rx="1.8" ry="4" fill="none" stroke="#111" stroke-width=".8"/><path d="M.5,4.5 H8.5" stroke="#111" stroke-width=".8"/></svg>
      www.orvellabio.com
    </span>
  </div>
  <div class="abs note"><span>For accurate results, please read</span><br>the instructions carefully before use</div>

  <!-- back panel -->
  <div class="abs brand-back">VitaCue<span class="tm">TM</span></div>
  <div class="abs badge badge-back">5 Tests/Kit</div>
  <div class="abs subtitle">10-Minute Canine<br>&amp; Feline Rapid Test Kit</div>
  <div class="abs species">For Dogs &amp; Cats</div>
  <div class="art art-pets-back" role="img" aria-label="Line drawing of a sitting dog and cat"></div>
  <div class="art art-dog-faint" role="img" aria-label="Faint silhouette of a sitting dog"></div>
  <div class="abs maker-back">Orvella</div>

  <!-- brand story side -->
  <div class="abs story">VitaCue is made by Orvella, our name joins 'Or' for light and clarity with "Vella" for care and vigilance, representing both intelligent efficacy in our science and reverence for the spirit of life ('Vita Orvella') in all creatures.</div>
</div>
</body>
</html>
```